Design a Mobile App for Landscape Businesses

This project is to design the first three screens for a mobile app for Landscape and Lawncare businesses. This app will serve as a directory for homeowners to locate landscape and lawn care businesses and for landscape businesses and contractors to run their business. See the attached PDF for more information and example
Here is the link to the description https://lnkshrt.example/q7Tz3K

Target Market(s)

Landscape and lawn care business, gardeners, home owners

Industry/Entity Type

Landscape Gardening

Logo Text

Velmarigo

Colors

Designer to choose colors to be used in the design.

```html
<!DOCTYPE html>
<html lang="en">
<head>
<meta charset="utf-8">
<title>Velmarigo – App Design</title>
<link href="https://fonts.googleapis.com/css2?family=Montserrat:wght@400;500;600;700;800&family=Quicksand:wght@500;600&display=swap" rel="stylesheet">
<style>
  :root {
    --brand-green: #16a45c;
    --brand-green-dark: #118a4c;
    --ink: #0f1f2b;
    --ink-soft: #3f4650;
    --text: #2a2a2a;
    --muted: #e8ebef;
    --white: #ffffff;
    --avatar-blue: #3f7fe0;
    --avatar-lime: #b7d63a;
    --accent-yellow: #f2c318;
    --accent-magenta: #d52fd6;
    --accent-pink: #e8356f;
    --accent-lime: #69cf1e;
    --accent-cyan: #12c8d6;
    --accent-blue: #2a7be6;
  }
  html, body { margin: 0; padding: 0; overflow: hidden; }
  body { width: 1200px; height: 1200px; background: var(--white); font-family: "Montserrat", sans-serif; position: relative; }

  .deco { position: absolute; }

  .headline { position: absolute; left: 700px; top: 150px; width: 440px; text-align: center; }
  .headline__name { font-family: "Montserrat", sans-serif; font-weight: 800; font-size: 60px; color: var(--ink); margin: 0; letter-spacing: -0.5px; }
  .headline__sub { font-family: "Quicksand", sans-serif; font-weight: 600; font-size: 36px; color: var(--ink-soft); margin: 6px 0 0; }

  .app-screen { position: absolute; left: 170px; top: 150px; width: 420px; height: 900px; background: var(--white); border-radius: 26px; overflow: hidden; box-shadow: 0 18px 50px rgba(60,90,160,0.18); }

  .status-bar { background: var(--brand-green); height: 30px; display: flex; align-items: center; justify-content: flex-end; gap: 10px; padding: 0 16px; color: var(--white); font-size: 13px; font-weight: 500; }
  .app-bar { background: var(--brand-green); height: 64px; display: flex; align-items: center; padding: 0 16px; color: var(--white); }
  .app-bar__title { font-size: 22px; font-weight: 600; margin-left: 26px; flex: 1; }
  .app-bar__actions { display: flex; gap: 22px; }

  .listing { padding: 18px 18px 20px; }
  .listing + .listing { border-top: 8px solid var(--muted); }
  .listing__head { display: flex; gap: 12px; }
  .listing__avatar { flex: none; width: 46px; height: 46px; border-radius: 50%; margin-top: 4px; }
  .listing__avatar--blue { background: var(--avatar-blue); }
  .listing__avatar--lime { background: var(--avatar-lime); }
  .listing__name { font-size: 19px; font-weight: 700; color: var(--text); margin: 0 0 6px; }
  .listing__blurb { font-size: 14px; line-height: 1.45; color: var(--text); margin: 0; }
  .listing__more { color: var(--brand-green); font-weight: 700; }
  .listing__photo { margin-top: 14px; height: 230px; border-radius: 16px; }
  .listing__photo--terraces { background: linear-gradient(160deg, #6d8f4a 0%, #4f9a32 40%, #c9a98c 60%, #3e7d2a 100%); }
  .listing__photo--flowerbeds { background: linear-gradient(170deg, #7aa24a 0%, #c73a3a 35%, #5f9a35 60%, #b8c9a0 100%); height: 270px; }

  .listing__meta { margin-top: 16px; display: grid; grid-template-columns: 1fr auto; gap: 10px 12px; align-items: center; }
  .meta-line { display: flex; align-items: center; gap: 12px; font-size: 15px; color: var(--text); font-weight: 500; }
  .meta-line--phone { color: var(--brand-green); font-weight: 600; font-size: 17px; }
  .quote-button { grid-row: 1 / span 2; grid-column: 2; align-self: center; background: var(--brand-green); color: var(--white); border: none; border-radius: 8px; padding: 12px 16px; font-family: "Montserrat", sans-serif; font-weight: 700; font-size: 15px; box-shadow: 0 3px 8px rgba(17,138,76,0.35); }
</style>
</head>
<body>

  <!-- decorative marks -->
  <svg class="deco" style="left:118px;top:163px" width="22" height="22" viewBox="0 0 22 22"><path d="M8 0h6v8h8v6h-8v8H8v-8H0V8h8z" fill="var(--accent-magenta)"/></svg>
  <svg class="deco" style="left:286px;top:134px" width="38" height="38" viewBox="0 0 38 38"><rect x="4" y="4" width="30" height="30" rx="13" fill="none" stroke="var(--accent-magenta)" stroke-width="7"/></svg>
  <svg class="deco" style="left:638px;top:104px" width="32" height="32" viewBox="0 0 32 32"><rect x="4" y="4" width="24" height="24" rx="11" fill="none" stroke="var(--accent-yellow)" stroke-width="6"/></svg>
  <svg class="deco" style="left:662px;top:221px" width="22" height="22" viewBox="0 0 22 22"><path d="M8 0h6v8h8v6h-8v8H8v-8H0V8h8z" fill="var(--accent-lime)"/></svg>
  <svg class="deco" style="left:80px;top:360px" width="32" height="32" viewBox="0 0 32 32"><rect x="4" y="4" width="24" height="24" rx="11" fill="none" stroke="var(--accent-yellow)" stroke-width="6"/></svg>
  <svg class="deco" style="left:1056px;top:728px" width="30" height="30" viewBox="0 0 30 30"><path d="M11 0h8v11h11v8H19v11h-8V19H0v-8h11z" fill="var(--accent-cyan)"/></svg>
  <svg class="deco" style="left:1086px;top:920px" width="32" height="32" viewBox="0 0 32 32"><rect x="4" y="4" width="24" height="24" rx="11" fill="none" stroke="var(--accent-yellow)" stroke-width="6"/></svg>
  <svg class="deco" style="left:868px;top:992px" width="38" height="38" viewBox="0 0 38 38"><rect x="4" y="4" width="30" height="30" rx="13" fill="none" stroke="var(--accent-pink)" stroke-width="7"/></svg>
  <svg class="deco" style="left:1034px;top:1034px" width="22" height="22" viewBox="0 0 22 22"><path d="M8 0h6v8h8v6h-8v8H8v-8H0V8h8z" fill="var(--accent-blue)"/></svg>

  <header class="headline">
    <h1 class="headline__name">Velmarigo</h1>
    <p class="headline__sub">App Design</p>
  </header>

  <main class="app-screen">
    <div class="status-bar">
      <svg width="14" height="12" viewBox="0 0 14 12"><path d="M0 0h14L7 12z" fill="currentColor"/></svg>
      <svg width="12" height="12" viewBox="0 0 12 12"><path d="M12 0v12H0z" fill="currentColor"/></svg>
      <svg width="8" height="13" viewBox="0 0 8 13"><rect x="0" y="1" width="8" height="12" rx="1" fill="currentColor"/></svg>
      <span>12:30</span>
    </div>
    <nav class="app-bar">
      <svg width="24" height="18" viewBox="0 0 24 18"><path d="M0 2h24M0 9h24M0 16h24" stroke="currentColor" stroke-width="2"/></svg>
      <span class="app-bar__title">Explore</span>
      <div class="app-bar__actions">
        <svg width="22" height="22" viewBox="0 0 22 22"><circle cx="9" cy="9" r="6.5" fill="none" stroke="currentColor" stroke-width="2.2"/><path d="M14 14l6 6" stroke="currentColor" stroke-width="2.4"/></svg>
        <svg width="24" height="22" viewBox="0 0 24 22"><path d="M0 2h14L8.5 10v8L5.5 16v-6z" fill="currentColor"/><path d="M16 4h8M16 9h8M16 14h6" stroke="currentColor" stroke-width="2"/></svg>
      </div>
    </nav>

    <article class="listing">
      <div class="listing__head">
        <span class="listing__avatar listing__avatar--blue"></span>
        <div>
          <h2 class="listing__name">Greenline Yardworks</h2>
          <p class="listing__blurb">Lorem Ipsum is simply dummy text of the printing and typesetting industry...<span class="listing__more">See More</span></p>
        </div>
      </div>
      <div class="listing__photo listing__photo--terraces" role="img" aria-label="Photo of terraced formal gardens with palms, lawns and a central stairway"></div>
      <div class="listing__meta">
        <div class="meta-line">
          <svg width="20" height="22" viewBox="0 0 20 22"><path d="M10 1a6 6 0 0 1 6 6c0 4.5-6 10-6 10S4 11.5 4 7a6 6 0 0 1 6-6z" fill="none" stroke="#777" stroke-width="1.8"/><circle cx="10" cy="7" r="2" fill="#777"/><path d="M2 21h16" stroke="#777" stroke-width="1.6"/></svg>
          <span>Ashbrook and the Surrounding Area</span>
        </div>
        <button class="quote-button">Request Quote</button>
        <div class="meta-line meta-line--phone">
          <svg width="20" height="20" viewBox="0 0 20 20"><path d="M4 1l4 4-2 3c1.5 3 3 4.5 6 6l3-2 4 4-3 3C8 18 2 12 1 4z" fill="#777"/></svg>
          <span>(555) 014-2290</span>
        </div>
      </div>
    </article>

    <article class="listing">
      <div class="listing__head">
        <span class="listing__avatar listing__avatar--lime"></span>
        <div>
          <h2 class="listing__name">Fernvale Gardens</h2>
          <p class="listing__blurb">All the Lorem Ipsum generators on the Internet tend to repeat predefined...<span class="listing__more">See More</span></p>
        </div>
      </div>
      <div class="listing__photo listing__photo--flowerbeds" role="img" aria-label="Photo of a hillside garden with colourful flowerbeds and stone steps"></div>
    </article>
  </main>

</body>
</html>
```